Prepared ready to cook meal delivery service needs a flyer design

We need a flyer design for a startup company based in Cape Town, South Africa. I've attached a few flyer designs that I like.

The company is called 'Brindle' and our website will be found at brindle.co.za. We don't have a logo yet.

Flyer text:

Brindle
Ready to roast

Do you feel like a home cooked meal but don't like shopping, peeling, chopping, cooking, or cleaning up?

We deliver ready to roast free range chicken and fresh vegetables to your door.

To order: SMS your name to 083 614 2958 and we'll call you back.

Only the best ingredients used
Free range chickens. Fresh herbs and vegetables. Virgin olive oil.

No bad carbs!

Ready to roast Free range chicken and fresh veggies
For 2 R99
For 4 R139
Updates

Wording of flyer updated.

Target Market(s)

Local Cape Townians that hate grocery shopping and need help saving time preparing meals.

Industry/Entity Type

Delivery Service

Requirements
Must have
• To find out more: SMS your name to 083 614 2958

```html
<!DOCTYPE html>
<html lang="en">
<head>
<meta charset="utf-8">
<title>Brindle – Ready to Roast Flyer</title>
<link rel="stylesheet" href="https://fonts.googleapis.com/css2?family=Bebas+Neue&family=Oswald:wght@400;500;600&family=Noto+Serif:ital,wght@0,700;1,700&family=Open+Sans:ital,wght@0,700;1,700&display=swap">
<style>
  :root {
    --page-bg: #f1f1f1;
    --photo-light: #e9883c;
    --photo-mid: #c4561f;
    --photo-dark: #7a2a10;
    --maroon: #5a1212;
    --deep-red: #8c1b17;
    --promo-red: #c7321f;
    --olive: #6d7a1c;
    --olive-text: #f3e24a;
    --cream: #e6ddd0;
    --price-yellow: #f5e03c;
    --band-cream: #ece6dd;
    --band-brown: #3b0f0f;
    --band-black: #111;
    --band-gold: #b9a11e;
    --white: #fff;
    --ink: #1d1210;
  }
  * { box-sizing: border-box; margin: 0; padding: 0; }
  html, body { width: 1200px; height: 831px; overflow: hidden; background: var(--page-bg); }
  .flyer {
    position: absolute; left: 302px; top: 0;
    width: 595px; height: 831px; overflow: hidden;
    background: var(--band-brown);
  }
  .hero-photo {
    position: absolute; left: 0; top: 0; width: 595px; height: 668px;
    background:
      radial-gradient(ellipse at 30% 40%, var(--photo-light) 0%, transparent 55%),
      radial-gradient(ellipse at 70% 70%, #d86a2a 0%, transparent 60%),
      linear-gradient(160deg, #d9722f 0%, var(--photo-mid) 50%, var(--photo-dark) 100%);
  }
  .dish-photo {
    position: absolute; left: 352px; top: -26px; width: 250px; height: 250px;
    border-radius: 50%; border: 5px solid var(--deep-red);
    background: radial-gradient(circle at 45% 55%, #d9a060 0%, #b3642a 45%, #7d2a15 80%, #3e6b2a 100%);
  }
  .intro {
    position: absolute; left: 34px; top: 30px; width: 340px;
    font: italic 700 18.5px/1.27 "Noto Serif", serif; color: var(--ink);
  }
  .brand-name {
    position: absolute; left: 36px; top: 128px;
    font: 400 84px/1 "Bebas Neue", sans-serif; color: var(--deep-red);
    letter-spacing: 2px;
  }
  .tagline {
    position: absolute; left: 32px; top: 214px;
    font: 400 64px/1 "Bebas Neue", sans-serif; color: var(--white);
    letter-spacing: 1px;
  }
  .badge {
    position: absolute; border-radius: 50%;
    display: flex; align-items: center; justify-content: center; text-align: center;
  }
  .badge-delivery {
    left: 20px; top: 286px; width: 226px; height: 226px;
    background: var(--promo-red); border: 5px solid var(--maroon);
    font: 400 20px/1.4 "Noto Serif", serif; color: var(--white);
    padding: 0 22px;
  }
  .badge-quality {
    left: 193px; top: 444px; width: 140px; height: 140px;
    background: var(--olive); border: 5px solid var(--maroon);
    font: 400 18px/1.45 "Oswald", sans-serif; color: var(--olive-text);
  }
  .badge-carbs {
    left: 247px; top: 570px; width: 98px; height: 98px;
    background: var(--cream); border: 5px solid var(--band-black);
    font: 500 17px/1.2 "Oswald", sans-serif; color: var(--ink);
  }
  .badge-price {
    background: var(--cream); border: 2px dashed var(--deep-red);
    box-shadow: 0 0 0 3px rgba(90,18,18,.5);
    font: 700 38px/1.05 "Noto Serif", serif; color: var(--price-yellow);
    -webkit-text-stroke: 1.4px var(--maroon);
  }
  .price-two { left: 327px; top: 283px; width: 136px; height: 136px; }
  .price-four { left: 369px; top: 400px; width: 156px; height: 156px; font-size: 42px; }
  .strap {
    position: absolute; left: 0; top: 668px; width: 595px; height: 43px;
    background: var(--band-cream); border-top: 3px solid var(--band-gold);
    font: 500 21px/40px "Oswald", sans-serif; color: var(--deep-red);
    text-align: center; text-transform: uppercase;
  }
  .order-bar { position: absolute; left: 0; top: 711px; width: 595px; height: 79px; background: var(--band-brown); }
  .order-label { position: absolute; left: 0; top: 0; height: 79px; }
  .order-label-text {
    position: absolute; left: 30px; top: 8px;
    font: italic 700 24px/1.3 "Open Sans", sans-serif; color: var(--white);
  }
  .order-text {
    position: absolute; left: 150px; top: 6px;
    font: 700 24px/1.4 "Open Sans", sans-serif; color: var(--white);
  }
  .order-text .second { padding-left: 26px; }
  .web-bar {
    position: absolute; left: 0; top: 790px; width: 595px; height: 41px;
    background: var(--band-gold);
    font: 500 24px/41px "Oswald", sans-serif; color: var(--maroon);
    text-align: center;
  }
</style>
</head>
<body>
<main class="flyer">
  <div class="hero-photo" role="img" aria-label="Close-up photo of a golden roasted chicken with herbs"></div>
  <div class="dish-photo" role="img" aria-label="Photo of roast chicken pieces with cherry tomatoes and basil"></div>

  <p class="intro">Do you feel like a home cooked meal but don't like shopping, peeling, chopping, cooking, or cleaning up?</p>
  <h1 class="brand-name">Brindle</h1>
  <h2 class="tagline">READY TO ROAST</h2>

  <div class="badge badge-delivery">We deliver ready to roast free range chicken and fresh vegetables to your door.</div>
  <div class="badge badge-quality">ONLY<br>THE BEST<br>INGREDIENTS<br>USE</div>
  <div class="badge badge-carbs">NO<br>BAD<br>CARBS!</div>
  <div class="badge badge-price price-two">for 2<br>R99</div>
  <div class="badge badge-price price-four">for 4<br>R139</div>

  <div class="strap">Ready to roast free range chicken and fresh veggies</div>

  <div class="order-bar">
    <svg class="order-label" width="170" height="79" viewBox="0 0 170 79" aria-hidden="true">
      <polygon points="0,0 170,0 130,79 0,79" fill="var(--band-black)"/>
    </svg>
    <div class="order-label-text">TO<br>ORDER:</div>
    <div class="order-text">SMS your name to 083 614 2958<br><span class="second">and we'll call you back.</span></div>
  </div>

  <div class="web-bar">WWW.BRINDLE.CO.ZA</div>
</main>
</body>
</html>
```